A new company focused on starting and investing in transformative businesses.

We need a simple and clean website with a few pages. we like larkmeadow.com as a starting point. we want the landing page to be very simple with an option to click through on the top right into INVESTOR LOGIN. then we want to be able to scroll down to see more about our company.

Target Market(s)

professional

Coding

Coded - Design and coding required

Number of Pages Required

2 page

Font styles to use
Serif
Sans Serif

Requirements
Must have
• HALVERN BUILDERS logo (attached as a file) on the top with INVESTOR LOGIN as a click through on the right. Please model the click through from larkmeadow.com. The description (also written in attached file) should be on the landing page. we do not want to have to scroll to read the description.

Then we can scroll down to read more about Halvern including the mission and the two types of businesses. More is detailed on the attached file called "Halvern Website Syntax"
Should not have
• should not be slow loading with lots of fancy graphics. should not be busy and with too many colors.

```html
<!DOCTYPE html>
<html lang="en">
<head>
<meta charset="utf-8">
<title>Halvern Builders</title>
<link href="https://fonts.googleapis.com/css2?family=Montserrat:wght@300;400;500;600;700;800&display=swap" rel="stylesheet">
<style>
:root{
  --navy:#0b1a4a;
  --navy-deep:#08123d;
  --navy-bar:#0d1a52;
  --blue:#1a73d9;
  --blue-soft:#2f8be6;
  --green:#22c55e;
  --ice:#eef3fb;
  --ice-2:#dfe9f5;
  --grey:#7b8290;
  --white:#ffffff;
  --hero-blue:#5b8fae;
}
*{box-sizing:border-box;margin:0;padding:0}
html,body{width:1200px;height:2802px;overflow:hidden;background:var(--white)}
body{position:relative;font-family:"Montserrat",sans-serif;color:var(--navy)}
.abs{position:absolute}

/* hero */
.hero{left:100px;top:95px;width:1000px;height:547px;background:linear-gradient(180deg,#6196b5 0%,#4f86a8 70%,#e9ecef 70%,#f2f3f4 100%);overflow:hidden}
.hero-photo{left:230px;top:0;width:540px;height:547px;background:radial-gradient(ellipse at 50% 45%,rgba(30,35,45,.55) 0%,rgba(30,35,45,.25) 45%,rgba(0,0,0,0) 70%)}
.hero-desk{left:0;top:380px;width:1000px;height:167px;background:linear-gradient(180deg,#e7eaee,#f5f6f7)}
.brand{display:flex;align-items:center;gap:8px}
.brand-mark{width:26px;height:26px;border-radius:3px}
.brand-name{font-weight:600;font-size:14px;line-height:1.05;letter-spacing:.3px}
.hero .brand{left:80px;top:18px}
.hero .brand-mark{background:var(--white)}
.hero .brand-name{color:var(--white)}
.login{left:814px;top:21px;width:103px;height:36px;background:var(--white);color:var(--navy);font-size:9px;font-weight:500;display:flex;align-items:center;justify-content:center;letter-spacing:.2px}
.hero-copy{left:154px;top:231px;border-left:3px solid var(--white);padding-left:16px;color:var(--white);font-size:29px;font-weight:300;line-height:34.5px;letter-spacing:.3px;text-transform:uppercase;width:560px}
.hero-copy b{font-weight:800}
.scroll{left:877px;top:210px;width:16px;height:260px}
.scroll span{position:absolute;left:0;top:0;writing-mode:vertical-rl;transform:rotate(180deg);font-size:8px;letter-spacing:2px;color:var(--white);font-weight:600}
.scroll i{position:absolute;left:7px;top:95px;width:1px;height:110px;background:rgba(255,255,255,.7)}
.scroll em{position:absolute;left:2px;top:228px;width:12px;height:20px;border:1.5px solid var(--white);border-radius:7px}

/* mission */
.mission-bg{left:100px;top:696px;width:1000px;height:627px;background:linear-gradient(180deg,var(--white) 0%,var(--white) 70%,#eef2f6 100%)}
.mission-band{left:100px;top:913px;width:230px;height:102px;background:var(--ice-2)}
.mission-arc{left:100px;top:1110px;width:490px;height:420px;border-radius:50%;background:#e8eef5;clip-path:inset(0 0 213px 0)}
.city{left:580px;top:1185px;width:520px;height:138px;background:linear-gradient(180deg,rgba(225,232,240,0) 0%,#d3dce6 60%,#c4ceda 100%)}
.person{left:152px;top:702px;width:414px;height:621px;background:linear-gradient(180deg,#e8e3de 0%,#3b4250 40%,#232a38 100%);border-radius:180px 180px 0 0}
.review{left:372px;top:1039px;width:219px;height:150px;background:var(--white);border-radius:6px;box-shadow:0 12px 30px rgba(11,26,74,.15)}
.review .badge{left:-27px;top:-25px;width:50px;height:50px;border-radius:50%;background:var(--green)}
.review h4{left:27px;top:22px;font-size:15px;font-weight:500;color:#111}
.review .ln{height:3px;background:#dbe6f5;border-radius:2px}
.review .ln.b{background:var(--blue);height:4px}
.review .r-brand{left:27px;top:118px;gap:5px}
.review .r-brand .brand-mark{width:12px;height:12px;background:var(--navy)}
.review .r-brand .brand-name{font-size:6px;color:var(--navy)}
.stars{left:120px;top:118px;font-size:10px;color:#f5b400;letter-spacing:1px}
.stars small{color:#333;font-size:7px;margin-left:4px}
.eyebrow{font-size:8.5px;font-weight:700;letter-spacing:2.2px;color:var(--blue);display:flex;align-items:center;gap:8px;text-transform:uppercase}
.eyebrow .rule{height:1px;background:var(--blue);display:block}
.mission-eyebrow{left:609px;top:851px}
.mission-title{left:609px;top:881px;border-left:2px solid var(--navy);padding-left:12px;font-size:24.5px;line-height:32px;font-weight:300;color:var(--navy);text-transform:uppercase}
.mission-title b{font-weight:800;display:block}
.mission-text{left:609px;top:963px;width:290px;font-size:13.5px;line-height:20px;color:var(--grey)}

/* types */
.types-bg{left:100px;top:1323px;width:1000px;height:820px;background:var(--ice)}
.types-eyebrow{left:0;top:1395px;width:1200px;justify-content:center}
.types-title{left:0;top:1424px;width:1200px;text-align:center;font-size:24.5px;line-height:32px;font-weight:300;color:var(--navy);text-transform:uppercase}
.types-title b{font-weight:800}
.card{top:1523px;width:337px;height:281px;background:var(--white);border-radius:8px;box-shadow:0 14px 30px rgba(11,26,74,.06);text-align:center}
.card.ground{left:254px}
.card.special{left:609px}
.card .icon{position:absolute;left:135px;top:27px;width:67px;height:67px;border-radius:50%}
.card.ground .icon{background:#e3f6ea}
.card.special .icon{top:30px;background:#e3edfa}
.card h3{position:absolute;left:0;width:100%;top:112px;font-size:13.5px;font-weight:700;letter-spacing:.4px;color:var(--navy)}
.card.special h3{top:116px}
.card p{position:absolute;left:34px;width:269px;top:144px;font-size:11.2px;line-height:18.8px;color:var(--grey)}
.card.special p{top:148px;left:36px;width:265px}
.hub{left:567px;top:1626px;width:68px;height:68px;border-radius:50%;background:var(--green);box-shadow:0 10px 22px rgba(34,197,94,.3)}

/* media */
.footer-bg{left:100px;top:2143px;width:1000px;height:501px;background:var(--navy-deep)}
.media{left:254px;top:1998px;width:691px;height:285px;border-radius:36px;background:linear-gradient(100deg,var(--blue) 0%,var(--blue-soft) 100%);overflow:hidden}
.media .glow{position:absolute;border-radius:50%;background:rgba(255,255,255,.06)}
.woman{left:653px;top:1844px;width:272px;height:439px;background:linear-gradient(180deg,#c99a6a 0%,#9ab8da 45%,#f1f3f6 85%);border-radius:130px 130px 0 0}
.media-eyebrow{left:291px;top:2053px;color:var(--white)}
.media-eyebrow .rule{background:rgba(255,255,255,.7)}
.media-title{left:291px;top:2078px;font-size:24.5px;line-height:32px;font-weight:300;color:var(--white);text-transform:uppercase}
.media-title b{font-weight:800}
.contact-label{left:291px;top:2161px;font-size:8.5px;font-weight:700;letter-spacing:2.2px;color:var(--white)}
.mail{left:291px;top:2188px;width:50px;height:50px;border-radius:50%;background:var(--white);display:flex;align-items:center;justify-content:center}
.mail-text{left:351px;top:2203px;font-size:15px;color:var(--white)}

/* footer */
.f-brand{left:252px;top:2380px}
.f-brand .brand-mark{background:var(--blue)}
.f-brand .brand-name{color:var(--white);font-size:14.5px}
.follow{left:252px;top:2434px;width:134px;display:flex;align-items:center;gap:8px;font-size:11px;font-weight:600;color:var(--white)}
.follow i{flex:1;height:1px;background:rgba(255,255,255,.3)}
.socials{left:266px;top:2467px;display:flex;gap:9px}
.socials span{width:18px;height:18px;border-radius:50%;background:var(--blue)}
.f-col h5{font-size:12px;font-weight:500;color:var(--white)}
.f-col h5::after{content:"";display:block;width:16px;height:2px;background:var(--white);margin-top:8px}
.f-col ul{list-style:none;margin-top:17px}
.f-col li{font-size:9px;letter-spacing:.4px;color:#c9d0e4;height:25px}
.c1{left:450px;top:2378px}
.c2{left:609px;top:2378px}
.c3{left:772px;top:2378px}
.c3 ul{margin-top:22px}
.c3 li{display:flex;align-items:flex-start;gap:12px;height:auto;margin-bottom:16px;letter-spacing:0;font-size:10px;line-height:13px;color:#c9d0e4}
.c3 li span.dot{width:20px;height:20px;border-radius:50%;background:var(--blue);flex:none;display:flex;align-items:center;justify-content:center}
.c3 li span.txt{padding-top:3px}
.copy{left:100px;top:2606px;width:1000px;height:38px;background:var(--navy-bar);font-size:8.5px;color:#9aa5c6;display:flex;align-items:center;justify-content:center}
</style>
</head>
<body>

<header class="abs hero">
  <div class="abs hero-desk"></div>
  <div class="abs hero-photo" role="img" aria-label="Photo of a businessman in a suit working at a desk with a laptop, lamp and plant"></div>
  <div class="abs brand"><span class="brand-mark"></span><span class="brand-name">HALVERN<br>BUILDERS</span></div>
  <a class="abs login">INVESTOR LOGIN</a>
  <h1 class="abs hero-copy">Halvern Builders is<br>an entrepreneurial firm<br>focused on <b>building</b> &amp;<br><b>growing transformational</b><br>companies</h1>
  <div class="abs scroll"><span>SCROLL DOWN</span><i></i><em></em></div>
</header>

<section>
  <div class="abs mission-bg"></div>
  <div class="abs mission-band"></div>
  <div class="abs mission-arc"></div>
  <div class="abs city" role="img" aria-label="Misty city skyline"></div>
  <div class="abs person" role="img" aria-label="Photo of a smiling man in glasses and a blazer holding a coffee cup"></div>
  <div class="abs review">
    <span class="abs badge"></span>
    <h4 class="abs">Halvern Builders</h4>
    <span class="abs ln" style="left:27px;top:55px;width:165px"></span>
    <span class="abs ln" style="left:27px;top:67px;width:88px"></span>
    <span class="abs ln" style="left:27px;top:78px;width:105px"></span>
    <span class="abs ln b" style="left:27px;top:90px;width:36px"></span>
    <span class="abs ln b" style="left:72px;top:90px;width:36px"></span>
    <div class="abs brand r-brand"><span class="brand-mark"></span><span class="brand-name">HALVERN<br>BUILDERS</span></div>
    <div class="abs stars">★★★★★<small>4.5</small></div>
  </div>
  <div class="abs eyebrow mission-eyebrow">Our Mission <span class="rule" style="width:128px"></span></div>
  <h2 class="abs mission-title">The mission of<b>Halvern Builders</b></h2>
  <p class="abs mission-text">Our mission is to build meaningful businesses that create enduring value by impacting people in a measurable way.</p>
</section>

<section>
  <div class="abs types-bg"></div>
  <div class="abs eyebrow types-eyebrow"><span class="rule" style="width:22px"></span>Our Mission<span class="rule" style="width:22px"></span></div>
  <h2 class="abs types-title">The <b>two types of</b><br><b>businesses</b> that Halvern Builders</h2>
  <article class="abs card ground">
    <span class="icon"><svg width="67" height="67" viewBox="0 0 67 67"><path d="M18 36 l8-6 8 4 8-4 7 6 -9 8 -6-4 -8 4z" fill="none" stroke="#22a355" stroke-width="1.6" stroke-linejoin="round"/><circle cx="35" cy="27" r="6" fill="#0b1a4a"/><path d="M32 27 l2 2 4-4" stroke="#fff" stroke-width="1.4" fill="none"/></svg></span>
    <h3>GROUND UP</h3>
    <p>Our ground up business applies a proven analytic process to identify value edge, a form of competitive advantage. We architect transformational companies and are deliberate in creating the foundation necessary to lead an industry</p>
  </article>
  <article class="abs card special">
    <span class="icon"><svg width="67" height="67" viewBox="0 0 67 67"><rect x="20" y="20" width="28" height="24" rx="2" fill="none" stroke="#1a73d9" stroke-width="1.6"/><line x1="20" y1="26" x2="48" y2="26" stroke="#1a73d9" stroke-width="1.6"/><circle cx="34" cy="37" r="6" fill="#0b1a4a"/><path d="M31 37 l2 2 4-4" stroke="#fff" stroke-width="1.4" fill="none"/></svg></span>
    <h3>SPECIAL OPPORTUNITIES</h3>
    <p>We partner with exceptional teams that create value by transforming lives. Our investment focus includes large companies and spin-outs.</p>
  </article>
  <span class="abs hub"></span>
</section>

<section>
  <div class="abs footer-bg"></div>
  <div class="abs media">
    <span class="glow" style="left:-40px;top:-90px;width:240px;height:240px"></span>
    <span class="glow" style="left:60px;top:60px;width:420px;height:420px"></span>
  </div>
  <div class="abs woman" role="img" aria-label="Photo of a smiling woman holding up a phone and pointing at it"></div>
  <div class="abs eyebrow media-eyebrow">For Media Inquiries <span class="rule" style="width:20px"></span></div>
  <h2 class="abs media-title">Halvern Builders for<br><b>media inquiries</b></h2>
  <p class="abs contact-label">PLEASE CONTACT</p>
  <span class="abs mail"><svg width="20" height="14" viewBox="0 0 20 14"><rect width="20" height="14" rx="1.5" fill="#0b1a4a"/><path d="M1 1 l9 7 9-7" stroke="#fff" stroke-width="1.4" fill="none"/></svg></span>
  <p class="abs mail-text">nora@halvernbuilders.com</p>
</section>

<footer>
  <div class="abs brand f-brand"><span class="brand-mark"></span><span class="brand-name">HALVERN<br>BUILDERS</span></div>
  <div class="abs follow"><i></i>Follow us<i></i></div>
  <div class="abs socials"><span></span><span></span><span></span><span></span></div>
  <nav class="abs f-col c1"><h5>Company</h5><ul><li>ELEMENTUM</li><li>VESTIBULUM</li><li>DONEC</li><li>MAURIS</li><li>PELLENTESQUE</li></ul></nav>
  <nav class="abs f-col c2"><h5>More link</h5><ul><li>MAECENAS</li><li>CONSECTETUR</li><li>TEMPUS</li></ul></nav>
  <div class="abs f-col c3"><h5>Get In Touch</h5>
    <ul>
      <li><span class="dot"><svg width="10" height="10" viewBox="0 0 10 10"><path d="M2 1 l2 0 1 2.5 -1.3 1 a6 6 0 0 0 2 2 l1-1.3 2.5 1 0 2 a1 1 0 0 1 -1 1 A8 8 0 0 1 1 2 a1 1 0 0 1 1-1z" fill="#fff"/></svg></span><span class="txt">555-014-2290</span></li>
      <li><span class="dot"><svg width="10" height="12" viewBox="0 0 10 12"><path d="M5 0 a4 4 0 0 1 4 4 c0 3-4 8-4 8 s-4-5-4-8 a4 4 0 0 1 4-4z" fill="#fff"/><circle cx="5" cy="4" r="1.5" fill="#1a73d9"/></svg></span><span class="txt">Etiam pharetra, erat sed<br>fermentum feugiat, velit mauris</span></li>
      <li><span class="dot"><svg width="10" height="8" viewBox="0 0 10 8"><rect width="10" height="8" rx="1" fill="#fff"/><path d="M.5 .5 l4.5 3.5 4.5-3.5" stroke="#1a73d9" fill="none"/></svg></span><span class="txt">hello@halvernbuilders.com</span></li>
    </ul>
  </div>
  <div class="abs copy">© 2021 Halvern Builders. ALL RIGHTS RESERVED.</div>
</footer>

</body>
</html>
```